Sphynx Cat Breeder

Hi.
I have just got a logo through Brand Harbor, and now I need a website.
I am home based Sphynx cat breeder (Velmira Sphynx)
I want to be able to show my breedings cats and kittens available for sale on my website.

Target Market(s)

Buyers of pet kittens in New Zealand, plus potentially buyers of kittens for breeding for overseas breeders

Industry/Entity Type

Crowd

Requirements
Must have
• Home page
About Us
My breeding Cats
Kittens
Caring for a Sphynx
Links
Contact (contact details plus a link to email)
I need to be able to upload photos as kittens come and go.
Nice to have
• A web counter, visible only to me, preferably showing which country they are from

```html
<!DOCTYPE html>
<html lang="en">
<head>
<meta charset="utf-8">
<title>Velmira Sphynx – Sphynx Cat Breeder</title>
<link href="https://fonts.googleapis.com/css2?family=Roboto+Condensed:wght@400;700&family=Ubuntu:wght@400;500;700&family=Arimo:wght@400;700&display=swap" rel="stylesheet">
<style>
  :root {
    --teal: #00bfd8;
    --teal-dark: #0098b0;
    --teal-deep: #007f94;
    --ink: #3f3f3f;
    --body: #555;
    --page: #efefef;
    --panel: #f4f4f4;
    --nav-dark: #1c1c1c;
  }
  * { box-sizing: border-box; margin: 0; padding: 0; }
  html, body { width: 1144px; height: 1200px; overflow: hidden; }
  body {
    background: repeating-linear-gradient(45deg, #f5f5f5 0 2px, #eeeeee 2px 4px);
    font-family: "Arimo", Arial, sans-serif;
    position: relative;
  }
  .site {
    position: absolute; left: 77px; top: 0; width: 996px; height: 1200px;
    background: #fff; box-shadow: 0 0 6px rgba(0,0,0,.12); overflow: hidden;
  }
  .abs { position: absolute; }

  /* header */
  .header { left: 0; top: 0; width: 996px; height: 175px;
    background: linear-gradient(#fff 0%, #fafafa 60%, #eeeeee 100%);
    border-top: 4px solid var(--teal); }
  .brand { left: 36px; top: 62px; display: flex; align-items: center; gap: 12px; }
  .brand-dot { width: 44px; height: 44px; border-radius: 50%; background: #1d1d1d; }
  .brand-name { font-family: "Ubuntu", sans-serif; font-weight: 500; font-size: 24px; color: #1d1d1d; }
  .follow { left: 740px; top: 48px; font-family: "Roboto Condensed", sans-serif; font-weight: 700;
    font-size: 23px; color: var(--teal); letter-spacing: .5px; }
  .social { top: 48px; width: 29px; height: 29px; border-radius: 6px; background: var(--teal-dark); }
  .main-nav { left: 243px; top: 115px; width: 750px; height: 41px; border-radius: 12px;
    background: linear-gradient(#3a3a3a, #111); display: flex; align-items: center; }
  .main-nav a { font-family: "Ubuntu", sans-serif; font-size: 14px; color: #fff; text-decoration: none;
    position: absolute; top: 12px; }
  .nav-sep { position: absolute; top: 4px; width: 1px; height: 33px; background: #050505; box-shadow: 1px 0 0 #444; }
  .nav-active { left: 264px; top: 106px; width: 97px; height: 58px; border-radius: 4px 4px 4px 4px;
    background: linear-gradient(#10cfe6, #00a6c0); display: flex; align-items: center; justify-content: center;
    font-family: "Ubuntu", sans-serif; font-size: 14px; color: #fff; }

  /* hero */
  .hero { left: 8px; top: 191px; width: 978px; height: 383px; border-radius: 20px;
    background: radial-gradient(ellipse at 55% 40%, #fff 0%, #f4f4f4 60%, #e4e4e4 100%); }
  .hero-title { left: 70px; top: 28px; font-family: "Roboto Condensed", sans-serif; font-weight: 700;
    font-size: 31px; color: var(--teal); letter-spacing: .3px; }
  .hero-sub { left: 70px; top: 66px; width: 410px; font-family: "Roboto Condensed", sans-serif; font-weight: 700;
    font-size: 25px; line-height: 35px; color: var(--ink); }
  .hero-copy { left: 73px; top: 152px; width: 388px; font-size: 12.5px; line-height: 20px; color: var(--body); text-align: justify; }
  .cta { left: 73px; top: 301px; width: 165px; height: 39px; border-radius: 20px;
    background: linear-gradient(#19d2e8, #0096b0); box-shadow: 0 2px 3px rgba(0,0,0,.2);
    display: flex; align-items: center; padding-left: 15px;
    font-family: "Roboto Condensed", sans-serif; font-weight: 700; font-size: 22px; color: #fff; }
  .cta-icon { position: absolute; right: 4px; top: 3px; width: 33px; height: 33px; border-radius: 50%;
    background: linear-gradient(#fafafa, #cfcfcf); }
  .hero-photo { left: 470px; top: 14px; width: 440px; height: 350px; border-radius: 40%;
    background: radial-gradient(ellipse at 50% 55%, #dcc1bf 0%, #e9d9d6 45%, rgba(244,244,244,0) 72%); }
  .arrow { width: 42px; height: 42px; border-radius: 50%; background: linear-gradient(#1ed3ea, #0088a0);
    box-shadow: 0 0 0 3px #fff, 0 2px 4px rgba(0,0,0,.3); }
  .arrow svg { display: block; }

  /* welcome */
  .welcome-title { left: 25px; top: 590px; font-family: "Roboto Condensed", sans-serif; font-weight: 700; font-size: 30px; color: var(--ink); }
  .welcome-title span { color: var(--teal); }
  .welcome-photo { left: 24px; top: 648px; width: 212px; height: 152px;
    background: linear-gradient(135deg, #c8c3c4, #e6ddd8 50%, #b9b5b8); box-shadow: 0 8px 8px -6px rgba(0,0,0,.35); }
  .copy { font-size: 12.5px; line-height: 20px; color: var(--body); text-align: justify; }
  .view-more { left: 582px; top: 887px; font-family: "Ubuntu", sans-serif; font-weight: 700; font-size: 13.5px; color: var(--teal-dark); }

  /* categories */
  .categories { left: 707px; top: 597px; width: 265px; height: 310px; border-radius: 20px;
    background: linear-gradient(#fff, #ececec); box-shadow: 0 0 3px rgba(0,0,0,.12); }
  .ribbon { left: 697px; top: 620px; width: 256px; height: 28px;
    background: linear-gradient(#1bd2ea, #00a9c3);
    clip-path: polygon(0 0, 100% 0, 92% 50%, 100% 100%, 0 100%);
    font-family: "Roboto Condensed", sans-serif; font-weight: 700; font-size: 21px; color: #fff; padding-left: 33px; line-height: 28px; }
  .ribbon-fold { left: 697px; top: 610px; width: 10px; height: 10px; background: var(--teal-deep); clip-path: polygon(100% 0, 100% 100%, 0 100%); }
  .cat-list { left: 725px; top: 662px; list-style: none; }
  .cat-list li { height: 30px; font-size: 13.5px; color: var(--body); display: flex; align-items: center; gap: 9px; }

  /* gallery */
  .gallery-tab { left: 29px; top: 928px; width: 179px; height: 32px;
    background: linear-gradient(#1bd2ea, #00a9c3); clip-path: polygon(0 0, 100% 0, 94% 100%, 0 100%);
    font-family: "Roboto Condensed", sans-serif; font-weight: 700; font-size: 20px; color: #fff; padding-left: 18px; line-height: 31px; letter-spacing: .3px;
    box-shadow: 0 4px 4px rgba(0,0,0,.2); }
  .thumb { width: 120px; height: 90px; box-shadow: 0 7px 6px -5px rgba(0,0,0,.4); }
  .caption { font-size: 10.5px; color: var(--body); text-decoration: underline; width: 140px; text-align: center; font-family: "Ubuntu", sans-serif; }
  .g-arrow { width: 34px; height: 34px; border-radius: 50%; background: linear-gradient(#1ed3ea, #0088a0);
    box-shadow: 0 0 0 3px #fff, 0 2px 4px rgba(0,0,0,.3); }

  /* footer */
  .footer { left: 0; top: 1143px; width: 996px; height: 63px; background: linear-gradient(#0fd0ea, #0098b0); }
  .footer-nav { position: absolute; top: 10px; left: 0; width: 100%; text-align: center;
    font-family: "Ubuntu", sans-serif; font-weight: 500; font-size: 13.5px; color: #fff; word-spacing: 2px; }
  .footer-nav a { color: #fff; text-decoration: none; }
  .footer-nav .tilde { margin: 0 26px; }
  .copyright { position: absolute; top: 37px; left: 0; width: 100%; text-align: center;
    font-family: "Ubuntu", sans-serif; font-weight: 500; font-size: 13.5px; color: #fff; }
</style>
</head>
<body>
<div class="site">

  <header class="abs header">
    <div class="abs brand"><span class="brand-dot"></span><span class="brand-name">Velmira Sphynx</span></div>
    <div class="abs follow">Follow us :</div>
    <span class="abs social" style="left:863px"></span>
    <span class="abs social" style="left:903px"></span>
    <span class="abs social" style="left:943px"></span>

    <nav class="abs main-nav">
      <span class="nav-sep" style="left:126px"></span>
      <a style="left:143px">About Us</a>
      <span class="nav-sep" style="left:225px"></span>
      <a style="left:253px">My breeding Cats</a>
      <span class="nav-sep" style="left:385px"></span>
      <a style="left:410px">Kittens</a>
      <span class="nav-sep" style="left:476px"></span>
      <a style="left:500px">Caring for a Sphynx</a>
      <span class="nav-sep" style="left:642px"></span>
      <a style="left:663px">Contact Us</a>
    </nav>
    <div class="abs nav-active">Home</div>
  </header>

  <section class="abs hero">
    <h1 class="abs hero-title">Sphynx cat breeder</h1>
    <h2 class="abs hero-sub">Cat and Kittens available for Sale on this websites</h2>
    <p class="abs hero-copy">Lorem Ipsum is simply dummy text of the printing and typesetting industry. Lorem Ipsum has been the industry's standard dummy text ever since the 1500s, when an unknown printer took a galley of type and scrambled it to make a type specimen book. It has survived not only five centuries, but also the leap into electronic typesetting, remaining essentially unchanged.</p>
    <div class="abs cta">Click Here
      <span class="cta-icon"><svg width="33" height="33" viewBox="0 0 33 33"><path d="M10 11l6 5.5-6 5.5M17 11l6 5.5-6 5.5" fill="none" stroke="#8a8a8a" stroke-width="2.5"/></svg></span>
    </div>
    <div class="abs hero-photo" role="img" aria-label="Photo of two Sphynx kittens, one sitting and one crouching"></div>
  </section>
  <div class="abs arrow" style="left:16px;top:362px"><svg width="42" height="42" viewBox="0 0 42 42"><path d="M25 12L14 21l11 9z" fill="#fff"/></svg></div>
  <div class="abs arrow" style="left:922px;top:362px"><svg width="42" height="42" viewBox="0 0 42 42"><path d="M17 12l11 9-11 9z" fill="#fff"/></svg></div>

  <h2 class="abs welcome-title"><span>Welcom to</span> Velmira Sphynx</h2>
  <div class="abs welcome-photo" role="img" aria-label="Photo of a spotted Sphynx kitten on a white rug"></div>
  <p class="abs copy" style="left:252px;top:648px;width:422px">Lorem Ipsum is simply dummy text of the printing and typesetting industry. Lorem Ipsum has been the industry's standard dummy text ever since the 1500s, when an unknown printer took a galley of type and scrambled it to make a type specimen book.</p>
  <p class="abs copy" style="left:252px;top:741px;width:422px">Lorem Ipsum is simply dummy text of the printing and typesetting industry. Lorem Ipsum has been the industry's standard dummy text ever since the 1500s, when an unknown printer took a galley</p>
  <p class="abs copy" style="left:23px;top:822px;width:651px">Lorem Ipsum is simply dummy text of the printing and typesetting industry. Lorem Ipsum has been the industry's standard dummy text ever since the 1500s, when an unknown printer took a galley of type and scrambled it to make a type specimen book. It has survived not only five centuries.</p>
  <a class="abs view-more">view more [+]</a>

  <aside class="abs categories"></aside>
  <div class="abs ribbon-fold"></div>
  <div class="abs ribbon">All Categories</div>
  <ul class="abs cat-list">
    <li><svg width="10" height="8" viewBox="0 0 10 8"><path d="M0 0l4 4-4 4zM5 0l4 4-4 4z" fill="#1bbfd8"/></svg>Aenean nonummy hendrerit</li>
    <li><svg width="10" height="8" viewBox="0 0 10 8"><path d="M0 0l4 4-4 4zM5 0l4 4-4 4z" fill="#1bbfd8"/></svg>Magnis dis parturient montes</li>
    <li><svg width="10" height="8" viewBox="0 0 10 8"><path d="M0 0l4 4-4 4zM5 0l4 4-4 4z" fill="#1bbfd8"/></svg>Mauris phasellus porta</li>
    <li><svg width="10" height="8" viewBox="0 0 10 8"><path d="M0 0l4 4-4 4zM5 0l4 4-4 4z" fill="#1bbfd8"/></svg>Morbi nunc odio, gravida at</li>
    <li><svg width="10" height="8" viewBox="0 0 10 8"><path d="M0 0l4 4-4 4zM5 0l4 4-4 4z" fill="#1bbfd8"/></svg>Nascetur ridiculus mus</li>
    <li><svg width="10" height="8" viewBox="0 0 10 8"><path d="M0 0l4 4-4 4zM5 0l4 4-4 4z" fill="#1bbfd8"/></svg>Nulla fusce feugiat malesuada</li>
    <li><svg width="10" height="8" viewBox="0 0 10 8"><path d="M0 0l4 4-4 4zM5 0l4 4-4 4z" fill="#1bbfd8"/></svg>Praesent vestibulum molestie</li>
    <li><svg width="10" height="8" viewBox="0 0 10 8"><path d="M0 0l4 4-4 4zM5 0l4 4-4 4z" fill="#1bbfd8"/></svg>Sociis natoque penatibus et</li>
  </ul>

  <div class="abs gallery-tab">Photo Gallery</div>
  <div class="abs g-arrow" style="left:18px;top:1021px"><svg width="34" height="34" viewBox="0 0 34 34"><path d="M21 9l-9 8 9 8z" fill="#fff"/></svg></div>
  <div class="abs g-arrow" style="left:949px;top:1021px"><svg width="34" height="34" viewBox="0 0 34 34"><path d="M13 9l9 8-9 8z" fill="#fff"/></svg></div>

  <div class="abs thumb" style="left:60px;top:997px;background:linear-gradient(135deg,#8a8490,#b9a9a6)" role="img" aria-label="Gallery photo of two Sphynx cats"></div>
  <div class="abs thumb" style="left:206px;top:997px;background:linear-gradient(135deg,#cbc6c2,#e4dbd4)" role="img" aria-label="Gallery photo of a spotted Sphynx kitten"></div>
  <div class="abs thumb" style="left:357px;top:997px;background:linear-gradient(135deg,#7e7f8a,#a9a9b3)" role="img" aria-label="Gallery photo of a grey Sphynx kitten"></div>
  <div class="abs thumb" style="left:513px;top:997px;background:linear-gradient(160deg,#f4f0ee,#d8c4bd)" role="img" aria-label="Gallery photo of a Sphynx kitten lying down"></div>
  <div class="abs thumb" style="left:665px;top:997px;background:linear-gradient(135deg,#bfbfc4,#dedad6)" role="img" aria-label="Gallery photo of a grey and white Sphynx kitten"></div>
  <div class="abs thumb" style="left:820px;top:997px;background:linear-gradient(135deg,#f1ecea,#cfb2ac)" role="img" aria-label="Gallery photo of a Sphynx cat portrait"></div>

  <span class="abs caption" style="left:45px;top:1107px">1st: Sphynx cat breeder</span>
  <span class="abs caption" style="left:189px;top:1107px">2nd: Sphynx cat</span>
  <span class="abs caption" style="left:347px;top:1107px">3rd: Sphynx cat breeder</span>
  <span class="abs caption" style="left:501px;top:1110px">4th: Sphynx cat</span>
  <span class="abs caption" style="left:638px;top:1110px">2nd: Sphynx cat</span>
  <span class="abs caption" style="left:805px;top:1110px">1st: Sphynx cat breeder</span>

  <footer class="abs footer">
    <div class="footer-nav"><a>Home</a><span class="tilde">~</span><a>About Us</a><span class="tilde">~</span><a>My breeding Cats</a><span class="tilde">~</span><a>Kittens</a><span class="tilde">~</span><a>Caring for a Sphynx</a><span class="tilde">~</span><a>Contact Us</a></div>
    <div class="copyright">Copyright @ 2012 velmirasphynx.example . All Right Reserved</div>
  </footer>
</div>
</body>
</html>
```